Flyer Design

I'm looking for a new flyer design to help promote our landscape company, and some of our main service for the up and coming season. We're trying to position ourselves as a leader in our market, so obviously quality is important to us.

Our current promotion is 25% off the first month with signup of annual service.

Phone Number: (816) 555-0193
Website: gardelvista.com
Our tagline: "Your hands are full... Let us help"

The call to action: direct them to our website for a detailed list of services and to receive a free quote.

You're welcome to add your own wording and punctuation. If I like the design I will provide feedback accordingly.

I have attached a jpg of our logo to help with design colors. I will provide the vector file upon completion of this project.

Also, I've attached a few photos that I had on hand of our companies work that may help with the design. Obviously I don't want to use them all, but there are a couple just to help out. I'm not opposed to stock photos either.
Thanks

Target Market(s)

We market to high end customers, generally with home between $500k-$2mil, or household income over $200k. Quality and creativity are most important to us.

Industry/Entity Type

Landscape

Requirements
Must have
• Creativity, easy to read, modern style.

```html
<!DOCTYPE html>
<html lang="en">
<head>
<meta charset="utf-8">
<title>Gardel Vista Flyer</title>
<link rel="stylesheet" href="https://fonts.googleapis.com/css2?family=Questrial&family=Montserrat:wght@600;700&family=Oleo+Script:wght@400;700&display=swap">
<style>
  :root {
    --stage: #a7a8b0;
    --paper: #f7f7f5;
    --orange: #d9560f;
    --orange-deep: #b8420a;
    --orange-text: #e07a1c;
    --ink: #58595b;
    --ink-soft: #7d7e80;
    --cream: #f6d7a3;
    --grass: #4f8a2c;
    --grass-light: #7bb04a;
    --sky: #b9d3ea;
    --wall: #c8b9a0;
    --shirt: #5a6f9c;
  }
  * { box-sizing: border-box; margin: 0; padding: 0; }
  html, body { width: 1200px; height: 900px; overflow: hidden; }
  body { background: var(--stage); font-family: "Questrial", sans-serif; position: relative; }

  .flyer {
    position: absolute; left: 296px; top: 20px;
    width: 608px; height: 860px;
    background: var(--paper); overflow: hidden;
  }

  .brand {
    position: absolute; left: 40px; top: 44px;
    display: flex; align-items: center; gap: 10px;
  }
  .brand-dot { width: 30px; height: 30px; border-radius: 50%; background: var(--orange); }
  .brand-name { font-size: 22px; color: var(--ink); letter-spacing: 1px; text-transform: uppercase; }

  .photo { position: absolute; }
  .photo-lawn-front {
    left: 92px; top: 130px; width: 288px; height: 200px;
    background: linear-gradient(180deg, var(--sky) 0%, var(--wall) 35%, var(--grass-light) 55%, var(--grass) 100%);
  }
  .photo-lawn-side {
    left: 380px; top: 28px; width: 208px; height: 182px;
    background: linear-gradient(180deg, var(--sky) 0%, var(--wall) 30%, var(--grass-light) 52%, var(--grass) 100%);
    border: 4px solid #fff;
  }

  .offer-tag { position: absolute; left: 386px; top: 214px; width: 210px; height: 124px; }
  .offer-text {
    position: absolute; left: 386px; top: 234px; width: 196px;
    text-align: center; color: #fff; font-family: "Oleo Script", serif; line-height: 1;
  }
  .offer-text .save { display: block; font-size: 24px; }
  .offer-text .amount { display: block; font-size: 40px; font-weight: 700; margin-top: 2px; }

  .tagline { position: absolute; left: 60px; top: 376px; width: 300px; text-align: center; }
  .tagline .line-one { display: block; font-family: "Montserrat", sans-serif; font-weight: 700; font-size: 18px; color: var(--ink); letter-spacing: .3px; }
  .tagline .line-two { display: block; font-size: 18px; color: var(--ink-soft); letter-spacing: 1px; margin-top: 2px; }
  .tagline .mark { color: var(--orange-text); font-family: "Montserrat", sans-serif; font-weight: 700; }

  .photo-customer {
    left: 378px; top: 400px; width: 200px; height: 206px;
    background: linear-gradient(180deg, var(--paper) 0%, #d8c6b4 30%, var(--shirt) 55%, #3f5580 100%);
    border-radius: 6px 6px 0 0;
  }

  .features { position: absolute; left: 100px; top: 470px; width: 270px; }
  .features h2 { font-family: "Montserrat", sans-serif; font-weight: 700; font-size: 17px; color: var(--orange-text); margin-bottom: 8px; }
  .features ul { list-style: none; }
  .features li { display: flex; align-items: center; gap: 8px; font-size: 12.5px; color: var(--ink-soft); margin-bottom: 5px; }
  .features svg { width: 11px; height: 11px; flex: none; }

  .footer-band { position: absolute; left: 0; top: 596px; width: 608px; height: 264px; }

  .about, .contact { position: absolute; color: var(--cream); font-size: 11.5px; line-height: 1.45; }
  .about { left: 100px; top: 668px; width: 270px; }
  .contact { left: 410px; top: 640px; width: 180px; }
  .about h3, .contact h3 { font-family: "Montserrat", sans-serif; font-weight: 700; font-size: 14px; color: #fff; text-decoration: underline; text-underline-offset: 3px; margin-bottom: 10px; }
  .about p, .contact p { margin-bottom: 8px; }
  .about .cta { color: #fff; }
</style>
</head>
<body>
  <main class="flyer">
    <div class="brand">
      <span class="brand-dot"></span>
      <span class="brand-name">Gardel Vista</span>
    </div>

    <div class="photo photo-lawn-front" role="img" aria-label="Freshly striped lawn in front of a single-storey commercial building"></div>
    <div class="photo photo-lawn-side" role="img" aria-label="Striped green lawn beside a two-storey building"></div>

    <svg class="offer-tag" viewBox="0 0 210 124" aria-hidden="true">
      <path d="M0 0 H196 V110 L210 124 H0 Z" fill="var(--orange)"/>
      <circle cx="98" cy="58" r="46" fill="none" stroke="#fff" stroke-width="1.5" stroke-dasharray="3 3"/>
    </svg>
    <div class="offer-text"><span class="save">Save</span><span class="amount">25%</span></div>

    <p class="tagline">
      <span class="line-one"><span class="mark">“</span>YOUR HANDS ARE FULL...</span>
      <span class="line-two">LET US HELP <span class="mark">”</span></span>
    </p>

    <div class="photo photo-customer" role="img" aria-label="Smiling man in a plaid shirt giving a thumbs up"></div>

    <section class="features">
      <h2>Our Services:</h2>
      <ul>
        <li><svg viewBox="0 0 12 12"><path d="M1 6 L4.5 9.5 L11 2" fill="none" stroke="var(--orange)" stroke-width="2.2"/></svg>Weekly mowing, edging and trimming</li>
        <li><svg viewBox="0 0 12 12"><path d="M1 6 L4.5 9.5 L11 2" fill="none" stroke="var(--orange)" stroke-width="2.2"/></svg>Seasonal cleanups and mulching</li>
        <li><svg viewBox="0 0 12 12"><path d="M1 6 L4.5 9.5 L11 2" fill="none" stroke="var(--orange)" stroke-width="2.2"/></svg>Landscape design and planting</li>
        <li><svg viewBox="0 0 12 12"><path d="M1 6 L4.5 9.5 L11 2" fill="none" stroke="var(--orange)" stroke-width="2.2"/></svg>Fertilizing and lawn care programs</li>
      </ul>
    </section>

    <svg class="footer-band" viewBox="0 0 608 264" preserveAspectRatio="none" aria-hidden="true">
      <defs>
        <linearGradient id="bandFill" x1="0" y1="0" x2="1" y2="1">
          <stop offset="0" stop-color="var(--orange)"/>
          <stop offset="1" stop-color="var(--orange-deep)"/>
        </linearGradient>
      </defs>
      <path d="M0 44 Q300 -4 608 10 V264 H0 Z" fill="url(#bandFill)"/>
    </svg>

    <section class="about">
      <h3>About us</h3>
      <p>Save 25% off your first month when you sign up for annual service.</p>
      <p class="cta">Visit gardelvista.com for a detailed list of services and your free quote.</p>
    </section>

    <section class="contact">
      <h3>Contact us</h3>
      <p>Phone: (816) 555-0193<br>Website: gardelvista.com</p>
    </section>
  </main>
</body>
</html>
```